Walkthrough Splash Page for new Content Management Site

Tallyroom.hive is a new site that helps groups and individuals design a custom site, create content and manage their members.

Although we have already designed a solid "root" homepage (see attached), we would like a set of default pages for when a person creates a new site that will help guide them through customizing their Space and creating content.

The "Root" Homepage is found here:
https://www.tallyroom.hive

An example of the current "default space" (which is what we need designed) can be found here:
https://freshroom.tallyroom.hive/

About the Functionality
This is some of the functionality that we would like covered in the design:
- A Tallyroom.hive Space is composed of two components: the "Space" and the "Dashboard".
- The Dashboard is used to (1) create content (e.g. Events, Auctions, Articles, Newsletters, etc.), (2) design the Space (by creating Pages, customizing the Menu and modifying overall styles), (3) view analytics about the space (e.g. how many members have viewed the space or have purchased a ticket, and (4) change their profile.
- User's can also use their profile to login/register for any other Tallyroom.hive Space as well.
- In the Dashboard you will see a "Profile" section and an "Account" section. The "Account" section is the User's relationship with the current Space. The "Profile" section will be follow the user around to any space that they are logged into.
- As you will see in the Dashboard, alot of the functionality has not yet been implemented, but please create the default page as if it has already been completed (it is coming soon).

Required Pages
We need four pages designed for the default new space: homepage, membership, about and contact.

The most important page is the default homepage which will help provide an example of what the user's Space can look and provide instructions on how to use the site (with links to the places on the site where these things can take place).

The default site also has a default "Membership", page which is a good change to demo another design to entire new people to sign up for the new Space as well as a "About" and "Contact" page.

We encourage you to visit our site (https://www.tallyroom.hive) to get a feel for our current design, which is based on Twitter Bootstrap and Vela Panel (http://skinvault.example/preview/QX7720391). To see a site that has already been created and customized, see the Harlow Ridge College Graduates Circle of New York (https://www.harlow-ridge.circle)

If you create a new Space you will see what the default page looks like (see attached).

I have also attached the Fonts, Icons and Color Palette that we currently use in the application - these are just to get you started, feel free to be creative!

Target Market(s)

Small groups, businesses and individuals who want to have an easy to way to create an online presence, especially those who wish to sell items online.

Industry/Entity Type

Management

Coding

Coded - Design and coding required

Number of Pages Required

4 page

Font styles to use
Serif
Other font styles liked:
• Movena Sans (Attached)

Colors
3276b5
33a6d7

Requirements
Must have
• Clean, tactile, responsive UI with pictures and diagrams.
• The site site takes on a high-tech, social approach to content management, which should be reflected in the design.

```html
<!DOCTYPE html>
<html lang="en">
<head>
<meta charset="utf-8">
<title>Tallyroom.hive – Space Home</title>
<link href="https://fonts.googleapis.com/css2?family=Open+Sans:wght@400;600;700&display=swap" rel="stylesheet">
<style>
:root{
  --blue:#3276b5;
  --blue-bar:#2f7bc2;
  --sky:#33a6d7;
  --page:#eeeaea;
  --card:#ffffff;
  --line:#e2e2e2;
  --ink:#222;
  --muted:#666;
  --red:#e8434a;
  --purple:#8a4fc2;
  --green:#6cb83c;
  --footer:#d5d3d3;
}
*{box-sizing:border-box;margin:0;padding:0}
html,body{width:826px;height:1200px;overflow:hidden}
body{background:var(--page);font-family:"Open Sans",Arial,sans-serif;color:var(--ink);position:relative;font-size:8px}
a{color:inherit;text-decoration:none}
.abs{position:absolute}

/* top bar */
.topbar{left:0;top:0;width:826px;height:28px;background:var(--blue-bar);color:#fff}
.brand{position:absolute;left:123px;top:5px;font-size:13px;font-weight:700}
.mainnav{position:absolute;left:285px;top:9px;display:flex;gap:17px;font-size:8px;font-weight:600}
.user{position:absolute;left:545px;top:8px;font-size:9px;font-weight:600;display:flex;align-items:center;gap:4px}
.btn-create{position:absolute;left:628px;top:6px;width:72px;height:18px;background:var(--green);border-radius:2px;font-size:8px;font-weight:600;display:flex;align-items:center;justify-content:center}

/* hero */
.hero{left:118px;top:28px;width:440px;height:161px;background:linear-gradient(180deg,#b7a863 0%,#6d6232 45%,#1e1a0f 100%)}
.tabs{left:118px;top:189px;width:440px;height:22px;background:var(--card);display:flex;gap:14px;padding-left:108px;align-items:center;font-size:7.5px}
.tabs .active{font-weight:600;position:relative}
.tabs .active::after{content:"";position:absolute;left:-2px;right:-2px;bottom:-7px;height:2px;background:var(--red)}
.avatar-frame{left:126px;top:116px;width:87px;height:86px;background:#fff;padding:3px}
.avatar{width:100%;height:100%;background:linear-gradient(160deg,#d9d2bd,#7b7460)}
.hero-name{left:219px;top:157px;color:#fff;font-size:12px}

/* right sidebar */
.side-feed{left:572px;top:30px;width:135px;height:182px;background:var(--card);padding:5px 6px}
.side-feed h3{font-size:9.5px;font-weight:400;color:var(--purple);padding-bottom:5px;border-bottom:1px solid var(--line);margin-bottom:5px}
.thumb{height:42px;position:relative}
.side-feed p{font-size:6.5px;color:var(--muted);line-height:1.35;margin:3px 0 6px}

/* left column cards */
.lcard{left:118px;width:137px;background:var(--card);border:1px solid #dcdcdc}
.lhead{height:18px;background:var(--blue-bar);color:#fff;font-size:8px;padding:0 18px;display:flex;align-items:center;justify-content:space-between}
.chev{width:6px;height:6px}
.lbody{padding:8px;font-size:7px;color:#444;line-height:1.4}
.welcome{top:222px;height:87px}
.welcome .wtitle{display:flex;gap:8px;padding:6px 8px;border-bottom:1px solid var(--line);font-size:8px;line-height:1.3}
.wtitle a{color:var(--blue)}
.dot-ic{width:14px;height:14px;border-radius:50%;background:var(--sky);flex:none}
.more{color:var(--red);text-align:right;display:block;margin-top:2px}
.item-row{display:flex;gap:8px;align-items:center;padding:7px 6px;border-bottom:1px solid #ececec;font-size:6.8px;color:#444;line-height:1.35}
.item-row:last-child{border-bottom:0}
.item-row .mk{width:22px;height:22px;border-radius:50%;flex:none}
.item-row .red{color:var(--red)}
.site-row{display:flex;align-items:center;gap:6px;padding:0 4px;height:38px;border-bottom:1px solid #ececec;font-size:7px;color:var(--red)}
.site-row .mk{width:12px;height:12px;border-radius:50%;flex:none}
.newsletter .lbody{font-size:7.5px}
.email{height:20px;border:1px solid #ddd;background:#eee;margin-top:9px;padding-left:6px;font-size:7px;color:#999;display:flex;align-items:center}
.subscribe{margin:8px 0 0 auto;width:50px;height:18px;background:var(--red);color:#fff;font-size:7.5px;display:flex;align-items:center;justify-content:center;border-radius:1px}
.gallery-grid{display:grid;grid-template-columns:repeat(3,1fr);gap:2px;padding:3px}
.gallery-grid div{height:42px}

/* middle / right cards */
.card{background:var(--card);border:1px solid #dcdcdc}
.card-photo{height:85px}
.card-head{height:28px;display:flex;align-items:center;justify-content:space-between;padding:0 14px;font-size:8px;border-bottom:1px solid var(--line)}
.card-head b{color:var(--blue);font-weight:600;margin-left:auto;margin-right:10px}
.faces{display:grid;grid-template-columns:repeat(5,1fr);gap:1px;height:85px;position:relative}
.faces div{background:linear-gradient(180deg,#d4c4b4,#8c7a6a)}
.faces div:nth-child(2n){background:linear-gradient(180deg,#b9a697,#5d4a3c)}
.pill{position:absolute;top:66px;background:#fff;font-size:6.5px;padding:2px 4px;border:1px solid #ccc}
.pill b{color:var(--blue);margin-left:5px}
.member{display:flex;align-items:center;gap:12px;height:47px;margin:0 8px;border-bottom:1px solid var(--line);font-size:8px}
.member:last-child{border-bottom:0}
.member .av{width:30px;height:30px;border-radius:50%;background:linear-gradient(160deg,#c9b6a3,#6e5b4d);flex:none}
.member small{display:block;font-size:7px;color:var(--muted);margin-top:3px}
.follow{margin-left:auto;border:1px solid #9cc3e4;color:var(--blue);font-size:6.5px;padding:2px 5px;border-radius:2px;background:#f4f9fd}
.event{display:flex;align-items:center;height:46px;margin:0 8px;border-bottom:1px solid var(--line)}
.event:last-child{border-bottom:0}
.date{width:30px;text-align:center;font-size:6.5px;color:var(--muted);border-right:1px solid var(--line);margin-right:10px;line-height:1.1}
.date b{display:block;font-size:10px;color:var(--ink)}
.event p{font-size:7px;color:#444;line-height:1.35}
.event .place{margin-top:3px;display:flex;align-items:center;gap:2px}
.auction{display:flex;align-items:center;gap:10px;height:51px;margin:0 8px;border-bottom:1px solid var(--line)}
.auction:last-child{border-bottom:0}
.auction .av{width:30px;height:30px;border-radius:50%;flex:none}
.auction h4{font-size:8.5px;font-weight:400}
.auction p{font-size:6.8px;color:var(--muted);line-height:1.3}
.auction .adate{margin-left:auto;border-left:1px solid var(--line);padding-left:8px;text-align:center;font-size:6.5px;color:var(--muted);line-height:1.1;width:36px;flex:none}
.adate b{display:block;font-size:10px;color:var(--purple);font-weight:600}
.amount{margin-left:auto;color:var(--purple);font-weight:600;font-size:9.5px}

/* posts */
.posts{left:265px;top:778px;width:442px;height:359px}
.posts .card-head{height:30px}
.view-all{color:var(--blue);font-weight:600;display:flex;align-items:center;gap:12px}
.post-grid{display:grid;grid-template-columns:repeat(3,136px);column-gap:11px;row-gap:6px;padding:6px 6px 0}
.post-img{height:60px;position:relative}
.by{position:absolute;right:3px;bottom:2px;background:rgba(255,255,255,.85);font-size:6.5px;color:#555;padding:1px 3px}
.post h4{font-size:8.5px;font-weight:400;margin:6px 4px 3px}
.post p{font-size:6.8px;color:#444;line-height:1.3;margin:0 4px;height:37px}
.post-meta{display:flex;align-items:center;gap:5px;border-top:1px solid var(--line);margin:6px 4px 0;padding-top:6px;font-size:6.5px;color:#999}
.post-meta .read{margin-left:auto;color:var(--ink);font-size:7.5px;margin-right:6px}
.ic{width:8px;height:6px;background:#bbb;display:inline-block}

.footer{left:0;top:1167px;width:826px;height:33px;background:var(--footer);font-size:7.5px;color:#444;padding:11px 0 0 129px}
</style>
</head>
<body>

<header class="abs topbar">
  <div class="brand">Tallyroom.hive</div>
  <nav class="mainnav"><a>HOME</a><a>MEMBERSHIP</a><a>ABOUT</a><a>CONTACT</a></nav>
  <div class="user">
    <svg width="11" height="12" viewBox="0 0 11 12"><circle cx="5.5" cy="3.5" r="3" fill="#fff"/><path d="M0 12c0-4 2.5-5 5.5-5s5.5 1 5.5 5z" fill="#fff"/></svg>
    Reed Alvar
    <svg width="7" height="5" viewBox="0 0 7 5"><path d="M0 0h7L3.5 4z" fill="#fff"/></svg>
  </div>
  <a class="btn-create">✚ Create Space</a>
</header>

<div class="abs hero" role="img" aria-label="Concert crowd with raised hands under warm stage lights"></div>
<div class="abs tabs"><span class="active">Profile</span><span>Members</span><span>Events</span><span>Auctions</span><span>Fundraisers</span></div>
<div class="abs avatar-frame"><div class="avatar" role="img" aria-label="Profile portrait of the space owner"></div></div>
<div class="abs hero-name">Reed Alvar</div>

<aside class="abs side-feed">
  <h3>Latest Auctions</h3>
  <div class="thumb" role="img" aria-label="Audience at an auction event" style="background:linear-gradient(135deg,#a78c79,#4e3d33)"></div>
  <p>Duis aute irure dolor in oluptate velit esse cillum dolore</p>
  <h3>Latest Events</h3>
  <div class="thumb" role="img" aria-label="Microphone at a conference" style="background:linear-gradient(135deg,#e6e1e6,#9a8f9c)"></div>
</aside>

<!-- left column -->
<section class="abs lcard welcome">
  <div class="wtitle"><span class="dot-ic"></span><span>Welcome to your new <a>Tallyroom.hive</a> Space!</span></div>
  <div class="lbody">This is your homepage, which helps to introduce who you are and what you are about.</div>
</section>

<section class="abs lcard" style="top:320px;height:82px">
  <div class="lhead">Bio <svg class="chev" viewBox="0 0 6 6"><path d="M1.5 0l3 3-3 3" stroke="#fff" fill="none" stroke-width="1.2"/></svg></div>
  <div class="lbody">Excepteur sint occaecat cupidatat non proident, sunt in culpa qui officia deserunt mollit anim id est laborum<a class="more">More</a></div>
</section>

<section class="abs lcard" style="top:413px;height:136px">
  <div class="lhead">My Spaces <svg class="chev" viewBox="0 0 6 6"><path d="M1.5 0l3 3-3 3" stroke="#fff" fill="none" stroke-width="1.2"/></svg></div>
  <div class="item-row"><span class="mk" style="background:#d9534f"></span><span>Excepteur sint occaecat cupidatat non <span class="red">[...]</span></span></div>
  <div class="item-row"><span class="mk" style="background:#f0a830"></span><span>Et voluptates repudiandae sint et molestiae <span class="red">[...]</span></span></div>
  <div class="item-row"><span class="mk" style="background:#33a6d7"></span><span>Et voluptates repudiandae sint et molestiae <span class="red">[...]</span></span></div>
</section>

<section class="abs lcard" style="top:559px;height:175px">
  <div class="lhead">My Ecommerce Sites <svg class="chev" viewBox="0 0 6 6"><path d="M1.5 0l3 3-3 3" stroke="#fff" fill="none" stroke-width="1.2"/></svg></div>
  <div class="site-row"><span class="mk" style="background:#2f7bc2"></span>www.plinkro.com</div>
  <div class="site-row"><span class="mk" style="background:#8a4fc2"></span>www.fernwick.com</div>
  <div class="site-row"><span class="mk" style="background:#f08a24"></span>www.tumblecube.com</div>
  <div class="site-row" style="border-bottom:0"><span class="mk" style="background:#33a6d7"></span>www.quietarc.com</div>
</section>

<section class="abs lcard newsletter" style="top:745px;height:120px">
  <div class="lhead">Newsletter <svg class="chev" viewBox="0 0 6 6"><path d="M1.5 0l3 3-3 3" stroke="#fff" fill="none" stroke-width="1.2"/></svg></div>
  <div class="lbody">Subscribe to our newsletter for latest updates
    <div class="email">Email...</div>
    <div class="subscribe">Subscribe</div>
  </div>
</section>

<section class="abs lcard" style="top:877px;height:154px">
  <div class="lhead">Gallery <svg class="chev" viewBox="0 0 6 6"><path d="M1.5 0l3 3-3 3" stroke="#fff" fill="none" stroke-width="1.2"/></svg></div>
  <div class="gallery-grid" role="img" aria-label="Grid of nine gallery photographs">
    <div style="background:#7a6a52"></div><div style="background:#8d8d8d"></div><div style="background:#a8887a"></div>
    <div style="background:#b8c2c6"></div><div style="background:#9a7660"></div><div style="background:#6f6f6f"></div>
    <div style="background:#c7b9a6"></div><div style="background:#a9a9a9"></div><div style="background:#4d4d4d"></div>
  </div>
</section>

<!-- members -->
<section class="abs card" style="left:265px;top:222px;width:215px;height:267px">
  <div class="faces" role="img" aria-label="Grid of member portrait photos">
    <div></div><div></div><div></div><div></div><div></div><div></div><div></div><div></div><div></div><div></div>
    <span class="pill" style="left:92px">Following<b>475</b></span>
    <span class="pill" style="left:153px">Followers<b>495</b></span>
  </div>
  <div class="card-head">Members<b>2384</b><svg width="6" height="8" viewBox="0 0 6 8"><path d="M1 0l4 4-4 4" stroke="#333" fill="none" stroke-width="1.3"/></svg></div>
  <div class="member"><span class="av" role="img" aria-label="Member photo"></span><div>Mira Solen<small>Similique sunt</small></div><span class="follow">Following</span></div>
  <div class="member"><span class="av" role="img" aria-label="Member photo"></span><div>Dane Corvel<small>Necessitatibus</small></div></div>
  <div class="member"><span class="av" role="img" aria-label="Member photo"></span><div>Owen Brisk<small>Exercitation Ullamco</small></div><span class="follow">Follow</span></div>
</section>

<!-- events -->
<section class="abs card" style="left:493px;top:222px;width:214px;height:267px">
  <div class="card-photo" role="img" aria-label="Conference hall with audience facing a stage screen" style="background:linear-gradient(180deg,#b89a78,#6e3b3a)"></div>
  <div class="card-head">Events<b>245</b><svg width="6" height="8" viewBox="0 0 6 8"><path d="M1 0l4 4-4 4" stroke="#333" fill="none" stroke-width="1.3"/></svg></div>
  <div class="event"><div class="date"><b>21</b>June</div><div><p>Quis autem vel eum iure reprehenderit qui in ea voluptate velit</p><p class="place"><svg width="5" height="7" viewBox="0 0 5 7"><path d="M2.5 7L0 3a2.5 2.5 0 1 1 5 0z" fill="#e8434a"/></svg>Reprehenderit qui</p></div></div>
  <div class="event"><div class="date"><b>19</b>June</div><div><p>Tempora incidunt ut labore et dolore magnam aliquam quaerat</p><p class="place"><svg width="5" height="7" viewBox="0 0 5 7"><path d="M2.5 7L0 3a2.5 2.5 0 1 1 5 0z" fill="#e8434a"/></svg>Eum fugiat</p></div></div>
  <div class="event"><div class="date"><b>15</b>June</div><div><p>Odio dignissimos ducimus qui blanditiis praesentium voluptatum</p><p class="place"><svg width="5" height="7" viewBox="0 0 5 7"><path d="M2.5 7L0 3a2.5 2.5 0 1 1 5 0z" fill="#e8434a"/></svg>Placeat Facere</p></div></div>
</section>

<!-- auctions -->
<section class="abs card" style="left:265px;top:501px;width:215px;height:266px">
  <div class="card-photo" role="img" aria-label="Ornate sofa set in a living room" style="background:linear-gradient(180deg,#a0764a,#5b3a22)"></div>
  <div class="card-head">Auctions<b>1575</b><svg width="6" height="8" viewBox="0 0 6 8"><path d="M1 0l4 4-4 4" stroke="#333" fill="none" stroke-width="1.3"/></svg></div>
  <div class="auction"><span class="av" role="img" aria-label="Auction item photo" style="background:#8b6a4a"></span><div><h4>Quasi architecto beatae</h4><p>Neque porro quisquam est qui voluptas sit aspernatur</p></div><div class="adate"><b>21</b>June</div></div>
  <div class="auction"><span class="av" role="img" aria-label="Auction item photo" style="background:#6e4a2c"></span><div><h4>Impedit quo minus id quod</h4><p>Voluptates repudiandae sint et molestiae non recusandae</p></div><div class="adate"><b>16</b>June</div></div>
  <div class="auction"><span class="av" role="img" aria-label="Auction item photo" style="background:#7a3a2a"></span><div><h4>Reiciendis voluptatibus</h4><p>Maiores alias consequatur aut perferendis doloribus</p></div><div class="adate"><b>10</b>June</div></div>
</section>

<!-- funds -->
<section class="abs card" style="left:493px;top:501px;width:214px;height:266px">
  <div class="card-photo" role="img" aria-label="Calculator and pen over a financial chart" style="background:linear-gradient(160deg,#2d5f8a,#b7cbe0)"></div>
  <div class="card-head">Fund Raised<b>$1250</b><svg width="6" height="8" viewBox="0 0 6 8"><path d="M1 0l4 4-4 4" stroke="#333" fill="none" stroke-width="1.3"/></svg></div>
  <div class="auction"><span class="av" role="img" aria-label="Fundraiser photo" style="background:#8b7f74"></span><div><h4>Excepteur sint occaecat</h4><p>Eum iure reprehenderit qui</p></div><span class="amount">$210</span></div>
  <div class="auction"><span class="av" role="img" aria-label="Fundraiser photo" style="background:#7e8f6a"></span><div><h4>Fugiat quo voluptas nulla</h4><p>Magni dolores eos qui ratione</p></div><span class="amount">$164</span></div>
  <div class="auction"><span class="av" role="img" aria-label="Fundraiser photo" style="background:#5c9a3c"></span><div><h4>Nisi ut aliquid ex commodi</h4><p>Architecto beatae vitae dicta sunt</p></div><span class="amount">$375</span></div>
</section>

<!-- posts -->
<section class="abs card posts">
  <div class="card-head">Latest Posts<span class="view-all">View All <svg width="6" height="8" viewBox="0 0 6 8"><path d="M1 0l4 4-4 4" stroke="#333" fill="none" stroke-width="1.3"/></svg></span></div>
  <div class="post-grid">
    <article class="post"><div class="post-img" role="img" aria-label="City skyline with towers by a river" style="background:linear-gradient(180deg,#9fb6c8,#4c6478)"><span class="by">Tess Marlow</span></div><h4>Ullamco laboris nisi</h4><p>Quia consequuntur magni dolores eos qui ratione voluptatem sequi nesciunt dicta sunt explicabo aute irure dolor in reprehenderit</p><div class="post-meta"><i class="ic"></i>22.06.2016<i class="ic"></i>10<span class="read">Read More</span></div></article>
    <article class="post"><div class="post-img" role="img" aria-label="Photographer holding a camera" style="background:linear-gradient(160deg,#d8d4cf,#6b5a4e)"><span class="by">Tess Marlow</span></div><h4>Nostrum exercitationem</h4><p>Similique sunt in culpa qui officia nimi id est laborum et dolorum fuga aut reiciendis voluptatibus maiores alias consequatur aut</p><div class="post-meta"><i class="ic"></i>22.06.2016<i class="ic"></i>10<span class="read">Read More</span></div></article>
    <article class="post"><div class="post-img" role="img" aria-label="City skyline with towers by a river" style="background:linear-gradient(180deg,#9fb6c8,#4c6478)"><span class="by">Tess Marlow</span></div><h4>Voluptatibus maiores alias</h4><p>Quia consequuntur magni dolores eos qui ratione voluptatem sequi nesciunt dicta sunt explicabo aute irure dolor in reprehenderit</p><div class="post-meta"><i class="ic"></i>22.06.2016<i class="ic"></i>10<span class="read">Read More</span></div></article>
    <article class="post"><div class="post-img" role="img" aria-label="City skyline with towers by a river" style="background:linear-gradient(180deg,#9fb6c8,#4c6478)"><span class="by">Tess Marlow</span></div><h4>Ullamco laboris nisi</h4><p>Quia consequuntur magni dolores eos qui ratione voluptatem sequi nesciunt dicta sunt explicabo aute irure dolor in reprehenderit</p><div class="post-meta"><i class="ic"></i>22.06.2016<i class="ic"></i>10<span class="read">Read More</span></div></article>
    <article class="post"><div class="post-img" role="img" aria-label="Photographer holding a camera" style="background:linear-gradient(160deg,#d8d4cf,#6b5a4e)"><span class="by">Tess Marlow</span></div><h4>Nostrum exercitationem</h4><p>Similique sunt in culpa qui officia nimi id est laborum et dolorum fuga aut reiciendis voluptatibus maiores alias consequatur aut</p><div class="post-meta"><i class="ic"></i>22.06.2016<i class="ic"></i>10<span class="read">Read More</span></div></article>
    <article class="post"><div class="post-img" role="img" aria-label="City skyline with towers by a river" style="background:linear-gradient(180deg,#9fb6c8,#4c6478)"><span class="by">Tess Marlow</span></div><h4>Voluptatibus maiores alias</h4><p>Quia consequuntur magni dolores eos qui ratione voluptatem sequi nesciunt dicta sunt explicabo aute irure dolor in reprehenderit</p><div class="post-meta"><i class="ic"></i>22.06.2016<i class="ic"></i>10<span class="read">Read More</span></div></article>
  </div>
</section>

<footer class="abs footer">©Copyright information here</footer>

</body>
</html>
```